Benefit Card for new Customers - LORVIX

We are planning our offline referral marketing programm. So we need a benefit card for new customers. We are a company that provides innovative and highly competent private tutoring for our customers. We are LORVIX (www.lorvix.ch) and are located in Bern (Switzerland). Our customers are schoolkids (and their parents), apprentices and students. Therefore we designed our corporate design for this target groups. Our corporate design is colourful (we use especially our corporate colours) and has as little edges as possible. As an illustration take a look at our website www.lorvix.ch where we tried to realize our corporate identity as suitable as possible.
We would like to see designs that use our corporate colours (green, blue and tourquois might be inviting colours). The final design should be inviting for new customers, highly professional and not too overloaded.

Dimensions of the card: 148 x 105 mm (millimeter) --> A6 Format
Font: Lato

Upload Files:
- Corporate colour codes
- rough draft of the benefit card
- text and wording document
- Logo

Target Market(s)

Schoolkids (and their parents), apprentices, students

Industry/Entity Type

Education

Requirements
Must have
• Clean Design, Font: Lato, right Dimension as mentioned in the despriction,
Should not have
• Edges

```html
<!DOCTYPE html>
<html lang="de">
<head>
<meta charset="utf-8">
<title>LORVIX Vorteils-Pass</title>
<link href="https://fonts.googleapis.com/css2?family=Lato:ital,wght@0,400;0,700;0,900;1,700&display=swap" rel="stylesheet">
<style>
  :root {
    --yellow: #f2be3c;
    --green: #9cc75a;
    --green-soft: #b5d585;
    --ink: #2e3138;
    --card: #f2f2f2;
    --stage: #e4e4e4;
    --faint-yellow: rgba(242, 190, 60, 0.16);
    --faint-green: rgba(156, 199, 90, 0.18);
  }
  * { box-sizing: border-box; margin: 0; padding: 0; }
  html, body {
    width: 1200px; height: 1000px; overflow: hidden;
    background: var(--stage);
    font-family: "Lato", Arial, sans-serif;
    color: var(--ink);
  }
  .benefit-card {
    position: absolute; left: 50px; top: 107px;
    width: 1100px; height: 785px;
    background: var(--card);
    overflow: hidden;
    border-radius: 6px;
  }
  .card-art { position: absolute; inset: 0; }
  .title-band {
    position: absolute; left: 0; top: 49px;
    width: 450px; height: 85px;
    background: var(--yellow);
    border-radius: 0 60px 60px 0;
    padding: 8px 0 0 51px;
  }
  .title-band h1 { font-size: 33px; font-weight: 900; line-height: 1.15; }
  .title-band p { font-size: 25px; line-height: 1.1; }
  .brand {
    position: absolute; right: 42px; top: 70px;
    display: flex; flex-direction: column; align-items: center; gap: 22px;
  }
  .brand-dot { width: 120px; height: 120px; border-radius: 50%; background: var(--yellow); }
  .brand-name { font-size: 52px; font-weight: 700; letter-spacing: 8px; color: var(--ink); }
  .lead {
    position: absolute; left: 51px; top: 218px;
    font-size: 28px; font-weight: 700; line-height: 38px;
  }
  .field-row {
    position: absolute; left: 51px;
    display: flex; align-items: baseline;
    font-size: 24px; white-space: nowrap;
  }
  .field-row.referrer { top: 354px; }
  .field-row.friend { top: 423px; }
  .fill-line { display: inline-block; height: 2px; background: var(--ink); margin: 0 8px; transform: translateY(-2px); }
  .referrer .fill-line { width: 284px; }
  .friend .fill-line { width: 318px; }
  .check-box {
    display: inline-block; width: 24px; height: 24px;
    border: 2px solid var(--ink); border-radius: 3px;
    margin: 0 16px 0 14px; transform: translateY(3px);
  }
  .invite {
    position: absolute; left: 51px; top: 518px;
    font-size: 22px; font-weight: 700;
  }
  .contact {
    position: absolute; right: 42px; top: 674px;
    text-align: right; font-size: 20px; line-height: 31px;
    font-style: normal;
  }
  .contact strong { font-weight: 700; }
  .pass-number {
    position: absolute; left: 51px; top: 734px;
    display: flex; align-items: baseline;
    font-size: 21px; font-weight: 700; font-style: italic;
  }
  .pass-number .fill-line { width: 205px; margin-left: 12px; }
</style>
</head>
<body>
  <article class="benefit-card">
    <svg class="card-art" viewBox="0 0 1100 785" width="1100" height="785" aria-hidden="true">
      <circle cx="440" cy="250" r="300" fill="var(--faint-yellow)"/>
      <circle cx="90" cy="640" r="230" fill="var(--faint-green)"/>
      <circle cx="730" cy="20" r="26" fill="var(--faint-yellow)"/>
      <circle cx="490" cy="600" r="20" fill="var(--faint-green)"/>
      <circle cx="530" cy="562" r="13" fill="var(--faint-green)"/>
      <circle cx="458" cy="200" r="5" fill="var(--yellow)"/>
      <path class="footer-band" d="M0,660 Q550,625 1100,660 L1100,785 L0,785 Z" fill="var(--green-soft)"/>
    </svg>

    <header class="title-band">
      <h1>Dein Vorteils-Pass</h1>
      <p>für bessere Noten</p>
    </header>

    <div class="brand">
      <span class="brand-dot"></span>
      <span class="brand-name">LORVIX</span>
    </div>

    <p class="lead">Mit diesem Vorteils-Pass schenken<br>wir Dir eine Unterrichtslektion.</p>

    <div class="field-row referrer">
      Empfehler/in:<span class="fill-line"></span>erhält Gratislektion<span class="check-box"></span>oder Kinogutschein<span class="check-box"></span>
    </div>
    <div class="field-row friend">
      Freund/in:<span class="fill-line"></span>erhält die vierte Lektion gratis.
    </div>

    <p class="invite">Melde Dich bei uns und lass Dich kostenlos und unverbindlich beraten.</p>

    <address class="contact">
      <strong>076 000 12 34</strong><br>
      <strong>www.lorvix.ch | hello@lorvix.ch</strong><br>
      weitere Infos: www.lorvix.ch/freundschaft
    </address>

    <div class="pass-number">Vorteils-Pass-Nr.<span class="fill-line"></span></div>
  </article>
</body>
</html>
```